Ferris Contracting LLC Business Card Design

I am looking for a creative and unique business card design. We are a commercial construction general contractor. With the name "FERRIS" Contracting, I am hoping to see some neat designs that correlate with the name.

```html
<!DOCTYPE html>
<html lang="en">
<head>
<meta charset="utf-8">
<title>Ferris Contracting LLC — Business Card</title>
<link href="https://fonts.googleapis.com/css2?family=Roboto:wght@700&family=Saira:wght@300;400;700&display=swap" rel="stylesheet">
<style>
  :root {
    --backdrop: #dedede;
    --card-dark: #232323;
    --card-dark-deep: #1b1b1b;
    --card-light: #ffffff;
    --brand-blue: #2188c9;
    --ink: #1c1c1c;
    --muted: #8a8a8a;
    --rule: #cfcfcf;
  }
  * { margin: 0; padding: 0; box-sizing: border-box; }
  html, body {
    width: 1200px;
    height: 1000px;
    overflow: hidden;
    background: var(--backdrop);
  }
  .canvas {
    position: relative;
    width: 1200px;
    height: 1000px;
  }
  .card {
    position: absolute;
    left: 329px;
    width: 542px;
    height: 313px;
    border-radius: 26px;
    overflow: hidden;
  }
  .card--front { top: 148px; background: var(--card-dark); }
  .card--back  { top: 514px; background: var(--card-light); }

  .front-pattern {
    position: absolute;
    inset: 0;
    background: linear-gradient(120deg, var(--card-dark-deep) 0%, var(--card-dark) 60%, #2a2a2a 100%);
  }
  .front-mark {
    position: absolute;
    left: 374px;
    top: 212px;
    display: flex;
    align-items: center;
    gap: 6px;
  }
  .mark-dot {
    width: 12px;
    height: 12px;
    border-radius: 50%;
    background: var(--brand-blue);
  }
  .mark-name {
    font-family: "Saira", sans-serif;
    font-weight: 700;
    color: var(--brand-blue);
    letter-spacing: 1px;
    line-height: 1;
  }
  .front-mark .mark-name { font-size: 26px; }

  .back-mark {
    position: absolute;
    left: 0;
    right: 0;
    top: 48px;
    display: flex;
    justify-content: center;
    align-items: center;
    gap: 10px;
  }
  .back-mark .mark-dot { width: 18px; height: 18px; }
  .back-mark .mark-name { font-size: 44px; }

  .identity {
    position: absolute;
    right: calc(542px - 249px);
    top: 166px;
    text-align: right;
  }
  .identity-name {
    font-family: "Roboto", sans-serif;
    font-weight: 700;
    font-size: 20px;
    color: var(--brand-blue);
    line-height: 22px;
  }
  .identity-title {
    font-family: "Saira", sans-serif;
    font-weight: 300;
    font-size: 18px;
    color: var(--muted);
    line-height: 22px;
  }
  .divider {
    position: absolute;
    left: 271px;
    top: 154px;
    width: 1px;
    height: 69px;
    background: var(--rule);
  }
  .contacts {
    position: absolute;
    left: 294px;
    top: 157px;
    list-style: none;
  }
  .contact {
    display: flex;
    align-items: center;
    gap: 9px;
    height: 22px;
    font-family: "Saira", sans-serif;
    font-weight: 400;
    font-size: 19px;
    color: var(--ink);
  }
  .contact svg { width: 12px; height: 12px; fill: var(--brand-blue); flex: none; }
</style>
</head>
<body>
<main class="canvas">
  <section class="card card--front" aria-label="Card front">
    <div class="front-pattern" role="img" aria-label="Dark embossed repeating company-name pattern"></div>
    <div class="front-mark">
      <span class="mark-dot"></span>
      <span class="mark-name">FERRIS</span>
    </div>
  </section>

  <section class="card card--back" aria-label="Card back">
    <div class="back-mark">
      <span class="mark-dot"></span>
      <span class="mark-name">FERRIS</span>
    </div>

    <div class="identity">
      <p class="identity-name">NAME SURNAME</p>
      <p class="identity-title">TITLE</p>
    </div>

    <div class="divider"></div>

    <ul class="contacts">
      <li class="contact">
        <svg viewBox="0 0 24 24" aria-hidden="true"><path d="M6.6 10.8c1.4 2.8 3.8 5.1 6.6 6.6l2.2-2.2c.3-.3.7-.4 1-.2 1.1.4 2.3.6 3.6.6.6 0 1 .4 1 1V20c0 .6-.4 1-1 1C10.6 21 3 13.4 3 4c0-.6.4-1 1-1h3.5c.6 0 1 .4 1 1 0 1.3.2 2.5.6 3.6.1.3 0 .7-.2 1L6.6 10.8z"/></svg>
        <span>(123) 456-7890</span>
      </li>
      <li class="contact">
        <svg viewBox="0 0 24 24" aria-hidden="true"><path d="M2 5h20v14H2V5zm2 2v.5l8 5 8-5V7H4zm0 2.8V17h16V9.8l-8 5-8-5z"/></svg>
        <span>name@website.com</span>
      </li>
      <li class="contact">
        <svg viewBox="0 0 24 24" aria-hidden="true"><path d="M12 2a10 10 0 1 0 0 20 10 10 0 0 0 0-20zm6.9 9h-3c-.1-2.2-.6-4.2-1.4-5.6A8 8 0 0 1 18.9 11zM12 4c.9 1 1.8 3.3 1.9 7h-3.8C10.2 7.3 11.1 5 12 4zM9.5 5.4C8.7 6.8 8.2 8.8 8.1 11h-3a8 8 0 0 1 4.4-5.6zM5.1 13h3c.1 2.2.6 4.2 1.4 5.6A8 8 0 0 1 5.1 13zM12 20c-.9-1-1.8-3.3-1.9-7h3.8c-.1 3.7-1 6-1.9 7zm2.5-1.4c.8-1.4 1.3-3.4 1.4-5.6h3a8 8 0 0 1-4.4 5.6z"/></svg>
        <span>website.com</span>
      </li>
    </ul>
  </section>
</main>
</body>
</html>
```